Business Card & Logo Design - Hedge Fund

We need a business card and logo design for a hedge fund. The hedge fund is named Morvane Equity LLC. Morvane Equity was created by finance professors and the strategy is based academic research that looks for patterns in stock prices. The design should look conservative, solid, strong. We favor a classic style - nothing flashy. The logo can relate to the name Morvane Equity, or it could involve a symbol design that connotes "science" . We are open to ideas. We do not want alot of colors - but if any, color - blue is preferred. The font that seems to look best for the name (Morvane Equity) is arial black. We are open to ideas. Most important - we want to see a mock up of an actual business card with the logo concept embedded. The business card should include space for : company name, individual name, position title, cell phone, address. We hope to have this work done by Sept. 8.

Target Market(s)

We will be meeting with and giving the business card to institutions and high net worth individuals.

Industry/Entity Type

Investment Advisory

Contact Information for Business Card

Company name - Morvane Equity LLC
Individual name - Peter Dalby
Title - Portfolio Manager
Cell - (412) 555-0187
Address - 2650 Birchmont Lane, Suite 300, Atlanta GA 30327

Font styles to use
Other font styles liked:
• Arial

Colors
3277b5
0255a3
85acd3
cedeed
fdf9cf
d9d9d9
e6e6e6
f04a50
6b449b

Requirements
Must have
• Must have card details that are sited above.
• We would like a logo related to the name (Morvane Equity) or concept of the fund.
Nice to have
• We want conservative / understated / clean crisp look.
• If any colors - we prefer conservative appearance - blue / gray.
• I have enclosed an example of a card style that looks attractive - please do not exactly copy this card. This is not our company or logo. I feel the layout is attractive - just as an example
Should not have
• Avoid too much color.
• I have selected some preferred colors. Please do not use all of the colors - I have selected a few that might work - but I am not sure. We are open to your ideas so please do not feel the need to use all or any of these.

```html
<!DOCTYPE html>
<html lang="en">
<head>
<meta charset="utf-8">
<title>Morvane Equity LLC — Business Card</title>
<link href="https://fonts.googleapis.com/css2?family=Lato:wght@400;700;900&display=swap" rel="stylesheet">
<style>
  :root {
    --backdrop: #d9d9d9;
    --card: #141516;
    --ink: #ffffff;
    --blue: #1f6fc4;
    --blue-soft: #3277b5;
  }
  * { box-sizing: border-box; margin: 0; padding: 0; }
  html, body { width: 1200px; height: 824px; overflow: hidden; }
  body {
    background: var(--backdrop);
    font-family: "Lato", Arial, sans-serif;
    color: var(--ink);
    position: relative;
  }
  .card {
    position: absolute;
    top: 257px;
    width: 540px;
    height: 310px;
    background: var(--card);
    border-radius: 4px;
    box-shadow: 0 10px 28px rgba(0,0,0,.25);
  }
  .card--front { left: 40px; }
  .card--back { left: 620px; }

  .wordmark {
    font-weight: 900;
    text-transform: uppercase;
    color: var(--ink);
    display: flex;
    align-items: center;
    gap: 10px;
    letter-spacing: .02em;
    line-height: 1.1;
  }
  .wordmark__square {
    width: 14px; height: 14px;
    background: var(--ink);
    flex: none;
  }

  .card--front .wordmark {
    position: absolute;
    left: 0; right: 0; top: 118px;
    justify-content: center;
    font-size: 30px;
  }
  .website {
    position: absolute;
    left: 0; right: 0; top: 188px;
    text-align: center;
    color: var(--blue);
    font-size: 15px;
    letter-spacing: .08em;
    text-transform: uppercase;
  }

  .card--back .wordmark {
    position: absolute;
    left: 26px; top: 122px;
    width: 190px;
    font-size: 22px;
    flex-wrap: nowrap;
  }
  .divider {
    position: absolute;
    left: 236px; top: 78px;
    width: 2px; height: 160px;
    background: var(--blue);
  }
  .contact {
    position: absolute;
    left: 262px; top: 84px;
    right: 20px;
  }
  .contact__name {
    font-weight: 900;
    font-size: 21px;
    text-transform: uppercase;
    letter-spacing: .03em;
  }
  .contact__title {
    color: var(--blue);
    font-size: 13px;
    text-transform: uppercase;
    letter-spacing: .06em;
    margin-bottom: 14px;
  }
  .contact__row {
    display: flex;
    align-items: flex-start;
    gap: 8px;
    font-size: 14px;
    line-height: 1.35;
    margin-bottom: 6px;
  }
  .contact__icon { width: 13px; height: 13px; flex: none; margin-top: 3px; fill: var(--blue); }
</style>
</head>
<body>
  <section class="card card--front" aria-label="Card front">
    <div class="wordmark"><span class="wordmark__square"></span>Morvane Equity LLC</div>
    <p class="website">www.morvaneequity.com</p>
  </section>

  <section class="card card--back" aria-label="Card back">
    <div class="wordmark"><span class="wordmark__square"></span>Morvane<br>Equity LLC</div>
    <div class="divider"></div>
    <div class="contact">
      <p class="contact__name">Peter Dalby</p>
      <p class="contact__title">Portfolio Manager</p>
      <p class="contact__row">
        <svg class="contact__icon" viewBox="0 0 24 24" aria-hidden="true"><path d="M6.6 10.8a15.1 15.1 0 0 0 6.6 6.6l2.2-2.2c.3-.3.7-.4 1-.2 1.1.4 2.3.6 3.6.6.6 0 1 .4 1 1V20c0 .6-.4 1-1 1C10.6 21 3 13.4 3 4c0-.6.4-1 1-1h3.5c.6 0 1 .4 1 1 0 1.3.2 2.5.6 3.6.1.3 0 .7-.2 1z"/></svg>
        (412) 555-0187
      </p>
      <p class="contact__row">
        <svg class="contact__icon" viewBox="0 0 24 24" aria-hidden="true"><path d="M2 5h20v14H2z M2 5l10 8 10-8" /></svg>
        pdalby@morvaneequity.com
      </p>
      <p class="contact__row">
        <svg class="contact__icon" viewBox="0 0 24 24" aria-hidden="true"><path d="M12 2a7 7 0 0 0-7 7c0 5.3 7 13 7 13s7-7.7 7-13a7 7 0 0 0-7-7zm0 9.5A2.5 2.5 0 1 1 12 6.5a2.5 2.5 0 0 1 0 5z"/></svg>
        <span>2650 Birchmont Lane,<br>Suite 300, Atlanta GA 30327</span>
      </p>
    </div>
  </section>
</body>
</html>
```